Upscale business cards needed for Board of Directors

We need professional business cards created for members of our family business Board of Directors. We would like these relatively simple and straightforward, but also with a unique element to set them apart. Probably stick with neutral and simple colors - white, grey etc. We need space for the traditional elements, including name, title, address, email/phone number. And we will be creating several from this template so it needs to be template that is easy to switch information in and out of.
Business
See description

```html
<!DOCTYPE html>
<html lang="en">
<head>
<meta charset="utf-8">
<title>Meridian Holdings Stationery</title>
<link href="https://fonts.googleapis.com/css2?family=Montserrat:wght@400;500;700&display=swap" rel="stylesheet">
<style>
  :root {
    --backdrop: #ececec;
    --paper: #ffffff;
    --ink: #1c1c1c;
    --muted: #6b6b6b;
    --gold: #b39f70;
  }
  * { box-sizing: border-box; margin: 0; padding: 0; }
  html, body { width: 1200px; height: 772px; overflow: hidden; }
  body {
    background: var(--backdrop);
    font-family: "Montserrat", Arial, sans-serif;
    color: var(--ink);
    position: relative;
  }

  /* Company name placeholder: one colour, one weight */
  .company-name {
    display: inline-block;
    font-weight: 700;
    color: var(--ink);
    line-height: 1.1;
    white-space: nowrap;
  }

  /* Letterhead */
  .letterhead {
    position: absolute; left: 80px; top: 70px;
    width: 440px; height: 622px;
    background: var(--paper);
    box-shadow: 0 2px 10px rgba(0,0,0,0.08);
  }
  .letterhead .company-name { position: absolute; left: 44px; top: 50px; font-size: 15px; }
  .letter {
    position: absolute; left: 44px; top: 120px; width: 352px;
    font-size: 7.6px; line-height: 1.55; color: #2a2a2a;
  }
  .letter__address { margin-bottom: 12px; }
  .letter p { margin-bottom: 10px; }
  .letter__signature { width: 82px; height: 24px; background: linear-gradient(90deg, #e6e6e6, #f2f2f2); margin: 6px 0 2px; }
  .letterhead__footer {
    position: absolute; right: 44px; bottom: 26px;
    text-align: right; font-size: 6.8px; color: var(--muted); line-height: 1.6;
  }
  .letterhead__footer strong { color: var(--ink); font-weight: 500; }
  .letterhead__bar { position: absolute; left: 0; right: 0; bottom: 0; height: 10px; background: var(--ink); }
  .letterhead__bar::after { content: ""; position: absolute; right: 0; top: -4px; width: 120px; height: 4px; background: var(--gold); }

  /* Business cards */
  .card {
    position: absolute; left: 650px; width: 420px; height: 240px;
    box-shadow: 0 2px 10px rgba(0,0,0,0.08);
    overflow: hidden;
  }
  .card--front { top: 140px; background: var(--paper); }
  .card--back { top: 440px; background: var(--gold); display: flex; align-items: center; justify-content: center; }
  .card--back .company-name { font-size: 26px; }

  .card--front .company-name { position: absolute; right: 30px; top: 40px; font-size: 18px; }
  .card__divider { position: absolute; left: 30px; right: 30px; top: 104px; height: 1px; background: var(--gold); }
  .card__person { position: absolute; left: 30px; top: 120px; }
  .card__name { font-size: 14px; font-weight: 700; letter-spacing: 0.06em; }
  .card__title { font-size: 8.5px; color: var(--muted); margin-top: 3px; letter-spacing: 0.05em; }
  .card__contact { position: absolute; left: 30px; top: 164px; font-size: 8.5px; line-height: 1.7; color: #333; }
  .card__web { position: absolute; right: 30px; top: 124px; font-size: 8.5px; color: #333; }
  .card__bar { position: absolute; left: 0; right: 0; bottom: 0; height: 10px; background: var(--ink); }
  .card__bar::after { content: ""; position: absolute; right: 0; top: -4px; width: 110px; height: 4px; background: var(--gold); }
</style>
</head>
<body>

  <section class="letterhead">
    <span class="company-name">Meridian Holdings</span>

    <div class="letter">
      <div class="letter__address">
        November 1, 2015<br>
        Mr. Peter Lowe<br>
        88 Elm Court<br>
        Fairview, OR 97024
      </div>
      <p>Dear Mr. Lowe,<br>
      The first paragraph of a typical business letter is used to state the main point of the letter. Begin with a friendly opening, then transition into the purpose of your letter in a couple of sentences.</p>
      <p>Beginning with the second paragraph, state the supporting details to justify your purpose. These may take the form of background information, statistics or first-hand accounts. A few short paragraphs within the body of the letter should be enough to support your reasoning.</p>
      <p>Finally, in the closing paragraph, briefly restate your purpose and why it is important. Consider ending your letter with your contact information, and close with gratitude for the reader's time.</p>
      <p>Sincerely,</p>
      <div class="letter__signature" role="img" aria-label="Handwritten signature of Arthur Hale"></div>
      <div>Arthur Hale<br>President</div>
    </div>

    <div class="letterhead__footer">
      <strong>www.meridianholdings.com | www.meridiangroup.com</strong><br>
      Meridian Holdings is a family-owned investment and property management group.
    </div>
    <div class="letterhead__bar"></div>
  </section>

  <section class="card card--front">
    <span class="company-name">Meridian Holdings</span>
    <div class="card__divider"></div>
    <div class="card__person">
      <div class="card__name">DANIEL HART</div>
      <div class="card__title">Chairman of the Board</div>
    </div>
    <div class="card__web">www.meridianholdings.com</div>
    <div class="card__contact">
      T: +1 555 014 2287<br>
      E: daniel@meridianholdings.com<br>
      48 Harbour Road, Suite 210, Portland
    </div>
    <div class="card__bar"></div>
  </section>

  <section class="card card--back">
    <span class="company-name">Meridian Holdings</span>
  </section>

</body>
</html>
```